Couples Workshop Flyer

I need a flyer to promote a one-day workshop for couples.

I am a therapist and life-coach and the session is called: "Lantern Bridge Days, and bring out the best in each other' - so Lantern Bridge Days is the bold name for the seminar but the point of the whole workshop is in the tagline, 'and bring out the best in each other'.

The final design should compel couples to take the risk to leave their comfort zones and attend a one-day workshop on a weekend .

Target Market(s)

Couples who are interested in self-improvement and identify with change and growth.
Somehow the flyer will match their aspirations!

Requirements
Should not have
• Not too many love hearts! :)
Not too gushy - a hint of romance!

```html
<!DOCTYPE html>
<html lang="en">
<head>
<meta charset="utf-8">
<title>Lantern Bridge Days – One Day Workshop for Couples</title>
<link href="https://fonts.googleapis.com/css2?family=Arimo:wght@400;700&display=swap" rel="stylesheet">
<style>
  :root {
    --sky: #92dbf8;
    --sky-shadow: #7cc4e4;
    --ink: #4b5866;
    --white: #ffffff;
    --frame: #5f6f7a;
    --portrait: #7fc6e6;
  }
  * { margin: 0; padding: 0; box-sizing: border-box; }
  html, body { width: 849px; height: 1200px; overflow: hidden; background: var(--sky); }
  .flyer {
    position: relative; width: 849px; height: 1200px; overflow: hidden;
    background: var(--sky);
    font-family: "Arimo", Arial, sans-serif; font-weight: 700;
  }
  .couple-area {
    position: absolute; left: 0; top: 320px; width: 390px; height: 880px;
  }
  .title, .tagline {
    position: absolute; color: var(--white);
    font-family: "Arimo", Arial, sans-serif; font-weight: 400; white-space: nowrap;
  }
  .title { left: 84px; top: 28px; font-size: 56px; letter-spacing: 0.5px; }
  .tagline { left: 250px; top: 120px; font-size: 27px; }
  .content { position: absolute; left: 184px; }
  .section-heading { color: var(--ink); font-size: 20.5px; white-space: nowrap; }
  .intro { top: 199px; width: 520px; }
  .intro p { color: var(--ink); font-size: 13px; line-height: 17px; }
  .intro .section-heading { margin-bottom: 16px; }
  .benefits { top: 350px; width: 505px; }
  .benefit-list { list-style: none; margin-top: 22px; }
  .benefit-list li {
    color: var(--white); font-size: 14.6px; line-height: 22px; margin-bottom: 23px;
  }
  .benefit-list li::before {
    content: ""; display: inline-block; width: 8px; height: 8px; background: var(--white);
    margin: 0 14px 1px 4px;
  }
  .bio { top: 941px; width: 372px; }
  .bio p {
    color: var(--ink); font-size: 11.6px; line-height: 14.6px; margin-bottom: 14px;
    text-align: justify;
  }
  .portrait {
    position: absolute; left: 592px; top: 943px; width: 108px; height: 160px;
    border: 2px solid var(--frame);
    background: linear-gradient(180deg, #a9e0f4 0%, var(--portrait) 100%);
  }
  .booking {
    position: absolute; left: 150px; width: 560px; top: 1133px; text-align: center;
    color: var(--white); font-size: 14.3px; line-height: 19px;
  }
</style>
</head>
<body>
<div class="flyer">
  <svg class="couple-area" role="img" aria-label="Silhouette of a couple standing side by side" viewBox="0 0 390 880">
    <defs>
      <linearGradient id="shadowFade" x1="0" y1="0" x2="0" y2="1">
        <stop offset="0" stop-color="#7cc4e4" stop-opacity="0.5"/>
        <stop offset="1" stop-color="#7cc4e4" stop-opacity="0.3"/>
      </linearGradient>
    </defs>
    <rect x="0" y="0" width="390" height="880" fill="url(#shadowFade)"/>
  </svg>

  <h1 class="title">Lantern Bridge Days...</h1>
  <p class="tagline">... and bring out the best in each other</p>

  <section class="content intro">
    <h2 class="section-heading">ONE DAY WORKSHOP FOR COUPLES</h2>
    <p>Some couples spend up big on their wedding day but fail to invest in their marriage or relationship, but relationships take much more than love to be successful.</p>
    <p>This innovative one-day seminar helps couples to breathe new life into their relationship.</p>
  </section>

  <section class="content benefits">
    <h2 class="section-heading">WHAT YOU WILL GAIN FROM DAN’S SEMINAR ?</h2>
    <ul class="benefit-list">
      <li>How to turn an argument into a moment of closeness – Easier than you think!</li>
      <li>Know what stress is doing to your relating and the two skillsets will make a big difference to each other’s stress-load.</li>
      <li>The role of pleasure in an emotionally-committed relationship and that’s more than sex!</li>
      <li>Identify the traps of committed relationships – and why being in a relationship doesn’t have to be a struggle.</li>
      <li>Learn how it’s not you or your partner’s fault - Identify the missing ingredients in your relationship and what you can do to get these back.</li>
      <li>What the research says about the ingredients of great sex</li>
      <li>What to do about the three drains on your relationship: boredom, having nothing to say and those same-old arguments. You will also practice using Dan’s negotiation tool that he developed for couples as well. Dan’s seminars are fun, informative and practical.</li>
    </ul>
  </section>

  <section class="content bio">
    <p>Daniel Marsh is a highly skilled couples therapist and educator, who is known for his innovative and creative approaches in his work. He has appeared on the Ch 4’s The Morning Circle show and Ch 6’s The Lounge as well as being interviewed on radio and in print.</p>
    <p>Dan’s seminars are run along brain-based education principles that he learnt from Dr Alan Whitcombe’s training in the USA, so that you will remember your new learning and integrate it into your life.</p>
  </section>

  <div class="portrait" role="img" aria-label="Portrait photograph of the workshop presenter"></div>

  <p class="booking">Take your relationship to the next level and book your seat now:<br>http://www.danielmarsh.com.au/couples.html</p>
</div>
</body>
</html>
```